Landscape design build company door flyer

I would like this flyer to convey a high-level of professionalism for a company that is excellent with communication with their clients as well as a company that does incredible installations

Went on vacation/holiday

```html
<!DOCTYPE html>
<html lang="en">
<head>
<meta charset="utf-8">
<title>Stillwater Builders – Door Hanger</title>
<link href="https://fonts.googleapis.com/css2?family=Heebo:wght@700&family=Montserrat:wght@400;500;700;800;900&family=Oswald:wght@700&display=swap" rel="stylesheet">
<style>
  :root {
    --page: #e7e7e7;
    --navy: #0f3445;
    --teal: #1d4a5c;
    --teal-soft: #2c6072;
    --yellow: #fcca3e;
    --mist: #dedede;
    --white: #ffffff;
    --ink: #0b1e29;
  }
  * { margin: 0; padding: 0; box-sizing: border-box; }
  html, body { width: 1200px; height: 1200px; overflow: hidden; }
  body { background: var(--page); position: relative; font-family: "Montserrat", sans-serif; }

  .hanger { position: absolute; top: 190px; width: 373px; height: 873px; overflow: hidden; background: var(--white); }
  .hanger--front { left: 208px; }
  .hanger--back { left: 630px; }

  .hero-photo { position: absolute; left: 0; top: 0; width: 100%; }
  .hanger--front .hero-photo { height: 580px; background: linear-gradient(180deg, #0f3446 0%, #224f60 40%, #1b4556 75%, #163c4c 100%); }
  .hanger--back .hero-photo { height: 420px; background: linear-gradient(180deg, #1b4759 0%, #2b5a6b 45%, #1f4c5e 100%); }

  .shapes { position: absolute; left: 0; top: 0; width: 373px; height: 873px; }

  .hang-hole { position: absolute; left: 135px; top: 32px; width: 104px; height: 104px; border-radius: 50%; background: var(--page); }

  .headline { position: absolute; left: 0; right: 0; top: 170px; text-align: center; font-family: "Heebo", sans-serif; font-weight: 700; font-size: 56px; line-height: 59px; color: var(--white); letter-spacing: -0.5px; }
  .headline .accent { color: var(--yellow); }

  .dots { position: absolute; top: 361px; left: 0; right: 0; display: flex; justify-content: center; gap: 9px; }
  .dots span { width: 8px; height: 8px; border-radius: 50%; background: var(--white); }
  .dots span.on { background: var(--yellow); }

  .lede { position: absolute; top: 386px; left: 30px; right: 30px; text-align: center; color: var(--white); font-size: 12.5px; line-height: 14px; }

  .brand { position: absolute; top: 560px; left: 0; right: 0; display: flex; align-items: center; justify-content: center; gap: 8px; }
  .brand-dot { width: 16px; height: 16px; border-radius: 50%; background: var(--navy); }
  .brand-name { font-family: "Montserrat", sans-serif; font-weight: 800; font-size: 22px; color: var(--navy); letter-spacing: 0.5px; }

  .service-area { position: absolute; top: 630px; left: 0; right: 0; text-align: center; font-weight: 800; font-size: 19px; line-height: 25.5px; color: var(--ink); }
  .service-note { position: absolute; top: 722px; left: 30px; right: 30px; text-align: center; font-size: 9.6px; line-height: 13.3px; color: var(--ink); }

  .cta { position: absolute; left: 30px; width: 314px; height: 44px; border-radius: 20px; background: var(--yellow); display: flex; align-items: center; justify-content: center; font-family: "Oswald", sans-serif; font-weight: 700; font-size: 24px; color: var(--ink); letter-spacing: -0.3px; }
  .hanger--front .cta { top: 774px; }
  .hanger--back .cta { top: 762px; }

  .site { position: absolute; left: 0; right: 0; text-align: center; font-weight: 700; font-size: 15px; letter-spacing: 3.6px; color: var(--ink); }
  .hanger--front .site { top: 826px; }
  .hanger--back .site { top: 814px; }

  .services-title { position: absolute; top: 210px; left: 0; right: 0; text-align: center; font-weight: 900; font-size: 32px; color: var(--yellow); letter-spacing: 0.3px; }

  .service-grid { position: absolute; left: 33px; top: 296px; display: grid; grid-template-columns: 145px 145px; column-gap: 14px; row-gap: 11px; }
  .service-tile { width: 145px; height: 136px; border: 2.5px solid var(--white); border-radius: 6px; overflow: hidden; background: var(--navy); display: flex; flex-direction: column; }
  .service-photo { flex: 1; }
  .service-label { height: 25px; background: var(--navy); color: var(--yellow); font-weight: 800; font-size: 9.6px; display: flex; align-items: center; justify-content: center; letter-spacing: 0.1px; }
  .photo-patio { background: linear-gradient(160deg, #3f4a3a, #8a8578 60%, #a89e90); }
  .photo-driveway { background: linear-gradient(180deg, #a59a86 0%, #8b4e28 50%, #b8aa98 100%); }
  .photo-wall { background: linear-gradient(180deg, #5a534d 0%, #6d6d6b 50%, #3f3f3f 100%); }
  .photo-deck { background: linear-gradient(180deg, #4e7a3a 0%, #5f8a45 45%, #8c4a2f 100%); }
  .photo-pool { background: linear-gradient(180deg, #c8d6de 0%, #9a7e62 40%, #46b6c6 100%); }
  .photo-fire { background: linear-gradient(180deg, #2f4a2a 0%, #8c8578 55%, #6f6a60 100%); }
</style>
</head>
<body>

<article class="hanger hanger--front">
  <div class="hero-photo" role="img" aria-label="Tinted photo of a traditional Japanese garden gate and temple roof"></div>
  <svg class="shapes" viewBox="0 0 373 873" aria-hidden="true">
    <path d="M0 562 L187 516 L373 562 L373 782 Q187 772 0 780 Z" fill="var(--mist)"/>
    <path d="M0 780 Q187 772 373 782 L373 873 L0 873 Z" fill="var(--white)"/>
  </svg>
  <div class="hang-hole"></div>

  <h1 class="headline">It’s Time<br><span class="accent">to Discover</span><br>Your Zen</h1>
  <div class="dots"><span></span><span class="on"></span><span></span></div>
  <p class="lede">From vision to reality, let us bring your dream outdoor space to life.</p>

  <div class="brand"><span class="brand-dot"></span><span class="brand-name">STILLWATER BUILDERS</span></div>

  <h2 class="service-area">PROUDLY SERVING CLIENTS<br>IN AND AROUND SEATTLE<br>SINCE 2018</h2>
  <p class="service-note">Headquartered in Sammamish, we typically consider projects in Eastside Seattle, including the areas of Bellevue, Issaquah, Kirkland, Redmond, and Sammamish</p>

  <div class="cta">CALL US NOW! (206) 555-0148</div>
  <p class="site">stillwaterbuilders.com</p>
</article>

<article class="hanger hanger--back">
  <div class="hero-photo" role="img" aria-label="Tinted photo of a modern home with a covered terrace and pool"></div>
  <svg class="shapes" viewBox="0 0 373 873" aria-hidden="true">
    <path d="M0 398 L187 340 L373 398 L373 873 L0 873 Z" fill="var(--white)"/>
  </svg>
  <div class="hang-hole"></div>

  <h2 class="services-title">OUR SERVICES</h2>

  <div class="service-grid">
    <div class="service-tile"><div class="service-photo photo-patio" role="img" aria-label="Paver patio with fire pit and lounge chairs"></div><div class="service-label">PAVER PATIOS</div></div>
    <div class="service-tile"><div class="service-photo photo-driveway" role="img" aria-label="Stone garage with wooden doors and paver driveway"></div><div class="service-label">PAVER DRIVEWAYS</div></div>
    <div class="service-tile"><div class="service-photo photo-wall" role="img" aria-label="Gray block retaining wall with steps"></div><div class="service-label">RETAINING WALLS</div></div>
    <div class="service-tile"><div class="service-photo photo-deck" role="img" aria-label="Wooden deck with red patio chairs among trees"></div><div class="service-label">DECKS &amp; RAILINGS</div></div>
    <div class="service-tile"><div class="service-photo photo-pool" role="img" aria-label="Modern house with a swimming pool"></div><div class="service-label">POOLS</div></div>
    <div class="service-tile"><div class="service-photo photo-fire" role="img" aria-label="Stone outdoor fireplace with burning fire"></div><div class="service-label">FIREPITS &amp; FIREPLACES</div></div>
  </div>

  <div class="cta">CALL US NOW! (206) 555-0148</div>
  <p class="site">stillwaterbuilders.com</p>
</article>

</body>
</html>
```